Design some Business Cards

Will leave good review!
I need business cards with a logo and contact information.
This company name is Tidewell Plumbing Corp. Its a new Massachusetts plumbing business. Tidewell is phone area code in Massachusetts. Results have to look professional and clean. Please submit business card examples and logo ideas.
I was thinking Tidewell being designed as digits on the phone keys. Try to use a black background(with decorations or not), the rest being gold. Try to do a double sided design. Just large logo on one side, same slightly smaller logo and contact information on the other.

Lets go, we are getting there! I really like your ideas so far, thank you, I have more work to be done!
I will leave a 5 star review to the winner!

```html
<!DOCTYPE html>
<html lang="en">
<head>
<meta charset="utf-8">
<title>Tidewell Plumbing Corp — Business Cards</title>
<link rel="stylesheet" href="https://fonts.googleapis.com/css2?family=Quicksand:wght@500;600;700&display=swap">
<style>
  :root {
    --backdrop: #2b2d31;
    --card-black: #1d1d1d;
    --card-orange: #f7941d;
    --text-light: #f2f2f2;
    --card-w: 640px;
    --card-h: 366px;
  }
  * { margin: 0; padding: 0; box-sizing: border-box; }
  html, body {
    width: 1200px;
    height: 900px;
    overflow: hidden;
    background: var(--backdrop);
    font-family: "Quicksand", sans-serif;
  }
  .sheet {
    width: 1200px;
    height: 900px;
    display: flex;
    flex-direction: column;
    align-items: center;
    justify-content: center;
    gap: 56px;
  }
  .card {
    position: relative;
    width: var(--card-w);
    height: var(--card-h);
    overflow: hidden;
    box-shadow: 0 12px 30px rgba(0,0,0,0.45);
  }
  .card-shape {
    position: absolute;
    inset: 0;
    width: 100%;
    height: 100%;
  }
  .shape-orange { fill: var(--card-orange); }
  .shape-black { fill: var(--card-black); }

  /* Front: large brand name */
  .front-brand {
    position: absolute;
    left: 0;
    right: 0;
    top: 118px;
    text-align: center;
    color: var(--card-orange);
    font-weight: 700;
    font-size: 40px;
    line-height: 1.1;
  }
  .front-web {
    position: absolute;
    left: 0;
    right: 0;
    top: 236px;
    text-align: center;
    color: var(--text-light);
    font-weight: 500;
    font-size: 13px;
    letter-spacing: 0.5px;
  }

  /* Back: contact side */
  .contact-list {
    position: absolute;
    left: 48px;
    top: 78px;
    list-style: none;
    display: flex;
    flex-direction: column;
    gap: 14px;
  }
  .contact-item {
    display: flex;
    align-items: center;
    gap: 14px;
    color: var(--text-light);
    font-weight: 500;
    font-size: 14px;
  }
  .contact-icon {
    width: 28px;
    height: 28px;
    background: var(--card-orange);
    display: flex;
    align-items: center;
    justify-content: center;
    flex-shrink: 0;
  }
  .contact-icon svg {
    width: 16px;
    height: 16px;
    fill: none;
    stroke: var(--card-black);
    stroke-width: 1.8;
    stroke-linecap: round;
    stroke-linejoin: round;
  }
  .divider {
    position: absolute;
    left: 318px;
    top: 128px;
    width: 2px;
    height: 110px;
    background: var(--card-orange);
  }
  .person {
    position: absolute;
    left: 350px;
    top: 150px;
  }
  .person-name {
    color: var(--card-orange);
    font-weight: 700;
    font-size: 24px;
  }
  .person-title {
    color: var(--text-light);
    font-weight: 500;
    font-size: 13px;
    margin-top: 2px;
  }
  .back-brand {
    margin-top: 16px;
    color: var(--card-orange);
    font-weight: 700;
    font-size: 17px;
    line-height: 1.15;
    width: 140px;
  }
</style>
</head>
<body>
<main class="sheet">

  <section class="card card-front" aria-label="Business card front">
    <svg class="card-shape" viewBox="0 0 640 366" preserveAspectRatio="none" aria-hidden="true">
      <rect class="shape-orange" width="640" height="366"/>
      <path class="shape-black" d="M70,0 L490,0 C545,70 590,120 640,140 L640,366 L250,366 C175,300 90,250 0,232 L0,52 C25,35 50,18 70,0 Z"/>
    </svg>
    <h1 class="front-brand">Tidewell<br>Plumbing Corp</h1>
    <p class="front-web">www.tidewellplumbing.com</p>
  </section>

  <section class="card card-back" aria-label="Business card back">
    <svg class="card-shape" viewBox="0 0 640 366" preserveAspectRatio="none" aria-hidden="true">
      <rect class="shape-orange" width="640" height="366"/>
      <path class="shape-black" d="M40,0 L410,0 C460,55 545,85 640,96 L640,366 L280,366 C200,296 100,262 0,250 L0,30 C14,20 28,10 40,0 Z"/>
    </svg>

    <ul class="contact-list">
      <li class="contact-item">
        <span class="contact-icon">
          <svg viewBox="0 0 24 24"><path d="M5 3h4l2 5-2.5 1.5a11 11 0 0 0 6 6L16 13l5 2v4a2 2 0 0 1-2 2A16 16 0 0 1 3 5a2 2 0 0 1 2-2z"/></svg>
        </span>
        +00 000 00000
      </li>
      <li class="contact-item">
        <span class="contact-icon">
          <svg viewBox="0 0 24 24"><rect x="3" y="5" width="18" height="14" rx="1"/><path d="M3 6l9 7 9-7"/></svg>
        </span>
        office@tidewellmail.com
      </li>
      <li class="contact-item">
        <span class="contact-icon">
          <svg viewBox="0 0 24 24"><path d="M12 21s-7-6.5-7-12a7 7 0 0 1 14 0c0 5.5-7 12-7 12z"/><circle cx="12" cy="9" r="2.5"/></svg>
        </span>
        Your Address in here
      </li>
    </ul>

    <div class="divider"></div>

    <div class="person">
      <p class="person-name">Marcus Delaney</p>
      <p class="person-title">Managing Director</p>
      <p class="back-brand">Tidewell Plumbing Corp</p>
    </div>
  </section>

</main>
</body>
</html>
```